Bramblewood Coatings of Central Florida, LLC. Start-up painting business needs a professional web desig

We have a start up painting business that would like to reach/focus on commercial clients like building contractors, HOA's, apartment complexes, etc.. We would like a residential aspect to the web design as well. We have an existing website at "trybramblewoodcoats.com" with usable content. Have logo and color scheme attached. Use provided website ONLY as template. Add commercial services page. Can type own content when needed.

Industry/Entity Type

Apartment

Number of Pages Required

5+ page

Font styles to use
Serif
Sans Serif
Decorative
Script

Requirements
Must have
• Commercial services

```html
<!DOCTYPE html>
<html lang="en">
<head>
<meta charset="utf-8">
<title>Bramblewood Coatings of Central Florida, LLC</title>
<link rel="stylesheet" href="https://fonts.googleapis.com/css2?family=Lato:wght@400;700&display=swap">
<style>
:root{
  --salmon:#e48f73;
  --olive:#6b6335;
  --ink:#2b2b2b;
  --body:#3a3a3a;
  --rule:#c9c9c9;
  --tile:#efefef;
  --white:#fff;
}
*{box-sizing:border-box;margin:0;padding:0}
html,body{width:974px;height:1200px;overflow:hidden;background:var(--white);font-family:'Lato',sans-serif;color:var(--body)}
.page{position:relative;width:974px;height:1200px}
.abs{position:absolute}
/* header */
.brand-mark{left:118px;top:22px;width:58px;height:58px;background:var(--salmon)}
.brand-name{left:190px;top:27px;font-size:20px;font-weight:700;line-height:24px;color:var(--salmon)}
.social{top:22px;width:24px;height:24px;border-radius:5px;background:#5c6b78}
.divider{left:727px;top:14px;width:1px;height:38px;background:#555}
.phone-icon{left:736px;top:23px}
.phones{left:765px;top:19px;font-size:13px;font-weight:700;line-height:16px;color:var(--ink)}
.nav{top:72px;font-size:13px;font-weight:700;color:var(--ink)}
.nav.active{color:var(--salmon);border-bottom:2px solid var(--salmon);padding-bottom:4px}
/* hero */
.hero{left:0;top:105px;width:974px;height:381px;background:linear-gradient(180deg,#8fb5d6 0%,#5f8da3 45%,#4a7489 100%)}
.hero-arrow{top:277px;width:30px;height:30px;border-radius:50%;background:var(--white)}
.hero-caption{left:100px;top:397px;width:383px;height:66px;background:rgba(40,50,60,.55);padding:3px 15px;color:var(--white);font-size:23px;font-weight:700;line-height:29px}
/* form */
.estimate{left:604px;top:436px;width:259px;height:172px;background:var(--white);border-radius:8px 8px 0 0;box-shadow:0 6px 14px rgba(0,0,0,.25)}
.estimate-title{left:618px;top:450px;font-size:19px;font-weight:700;color:var(--ink)}
.field{left:622px;width:223px;height:25px;border:1px solid #cfcfcf;border-radius:3px;background:var(--white);font-size:10px;font-weight:700;color:#555;padding:6px 13px}
.field.area{height:44px;box-shadow:0 2px 4px rgba(0,0,0,.25)}
.captcha-label{left:624px;top:634px;font-size:10px;font-weight:700;color:#555}
.submit{left:622px;top:687px;width:223px;height:35px;border-radius:6px;background:var(--olive);color:var(--white);font-size:14px;font-weight:700;text-align:center;line-height:35px}
.privacy{left:659px;top:734px;font-size:8px;color:#777}
/* intro */
.intro-title{left:111px;top:508px;width:400px;font-size:23px;font-weight:700;line-height:30px;color:var(--salmon)}
.rule{height:1px;background:var(--rule)}
.accent{height:2px;background:var(--salmon)}
.intro-copy{left:114px;top:589px;width:454px;font-size:12px;line-height:20.5px;letter-spacing:.3px}
.intro-copy p{margin:0}
/* services */
.services-title{left:0;top:773px;width:990px;text-align:center;font-size:23px;font-weight:700;color:var(--salmon)}
.tile{width:187px;height:129px}
.tile.text{background:var(--tile);text-align:center;padding:12px 12px 0}
.tile h3{font-size:17px;font-weight:700;color:var(--salmon);line-height:24px}
.tile .bar{width:54px;height:2px;background:var(--salmon);margin:2px auto 7px}
.tile p{font-size:11px;line-height:16px;color:var(--ink);height:48px;overflow:hidden}
.tile a{display:inline-block;margin-top:5px;font-size:11px;font-weight:700;color:var(--ink);text-decoration:underline}
/* footer */
.footer{left:0;top:1135px;width:974px;height:28px;background:var(--olive);color:var(--white);font-size:11px}
.footer-links{left:114px;top:7px}
.copyright{right:113px;top:7px}
</style>
</head>
<body>
<div class="page">
  <header>
    <div class="abs brand-mark"></div>
    <div class="abs brand-name">Bramblewood Coatings of<br>Central Florida, LLC</div>
    <div class="abs social" style="left:601px"></div>
    <div class="abs social" style="left:632px"></div>
    <div class="abs social" style="left:663px"></div>
    <div class="abs social" style="left:694px"></div>
    <div class="abs divider"></div>
    <svg class="abs phone-icon" width="22" height="22" viewBox="0 0 22 22"><circle cx="11" cy="11" r="10" fill="none" stroke="#8a7a2a" stroke-width="1.5"/><path d="M7 6c1-1 2 0 2.5 1.5l-1 1.2c.6 1.6 2 3 3.6 3.6l1.2-1c1.5.5 2.5 1.5 1.5 2.5-1 1.2-3 1.2-5-.5S5.8 8.5 7 6z" fill="#8a7a2a"/></svg>
    <div class="abs phones">+1.863-555-0142<br>+1.863-555-0178</div>
    <nav>
      <span class="abs nav active" style="left:538px">Home</span>
      <span class="abs nav" style="left:616px">About Us</span>
      <span class="abs nav" style="left:710px">Services</span>
      <span class="abs nav" style="left:800px">Contact Us</span>
    </nav>
  </header>

  <section>
    <div class="abs hero" role="img" aria-label="Photo of painters on ladders painting a blue house exterior"></div>
    <svg class="abs hero-arrow" style="left:43px" viewBox="0 0 30 30"><path d="M17 9l-6 6 6 6" fill="none" stroke="#444" stroke-width="1.3"/></svg>
    <svg class="abs hero-arrow" style="left:900px" viewBox="0 0 30 30"><path d="M13 9l6 6-6 6" fill="none" stroke="#444" stroke-width="1.3"/></svg>
    <div class="abs hero-caption">Lorem ipsum dolor sit amet,<br>consectetuer adipiscing elit sed</div>
  </section>

  <section>
    <div class="abs estimate"></div>
    <div class="abs estimate-title">SCHEDULE FREE ESTIMATE</div>
    <div class="abs field" style="top:484px">Full Name</div>
    <div class="abs field" style="top:516px">Email Address</div>
    <div class="abs field" style="top:549px">Phone&nbsp; Number</div>
    <div class="abs field area" style="top:582px">Decribe what needs to be done.</div>
    <div class="abs captcha-label">Please type the following</div>
    <div class="abs field" style="top:654px;font-weight:400">4&nbsp;&nbsp;&nbsp; 5&nbsp;&nbsp;&nbsp;&nbsp;&nbsp; 4&nbsp;&nbsp;&nbsp;&nbsp;&nbsp; 454</div>
    <div class="abs submit">SUBMIT NOW</div>
    <svg class="abs" style="left:659px;top:733px" width="9" height="10" viewBox="0 0 9 10"><rect x="1" y="4" width="7" height="6" fill="#777"/><path d="M2.5 4V3a2 2 0 0 1 4 0v1" fill="none" stroke="#777"/></svg>
    <div class="abs privacy" style="left:673px">Your information will never be shared</div>
  </section>

  <section>
    <h1 class="abs intro-title">The best home painters are yours for the taking.</h1>
    <div class="abs rule" style="left:111px;top:575px;width:457px"></div>
    <div class="abs accent" style="left:111px;top:574px;width:78px"></div>
    <div class="abs intro-copy">
      <p>Bramblewood Coatings of Central Florida, LLC. has painted thousands of homes in its day, but the one we're most excited about painting is the one we're painting today. Your home could be that home.</p>
      <p style="margin-top:3px">Know what you want? Great. We love to execute on a homeowner's vision. Not sure whether to go mild or wild? That's where our consultative approach and vast experience shines. We'll come up with a concept that you'll love, and then we'll make it happen.</p>
    </div>
  </section>

  <section>
    <h2 class="abs services-title" style="left:0;width:990px">Our Services</h2>
    <div class="abs rule" style="left:259px;top:807px;width:456px"></div>
    <div class="abs accent" style="left:449px;top:806px;width:76px"></div>

    <div class="abs tile text" style="left:112px;top:824px"><h3>Repair</h3><div class="bar"></div><p>No matter what the project you can always bet there will be repairs needed to provide the best job. We</p><a>READ MORE</a></div>
    <div class="abs tile" style="left:299px;top:824px;background:linear-gradient(180deg,#b8406a,#d4607f 75%,#e2e2e2)" role="img" aria-label="Photo of a pink living room with a sofa and shelves"></div>
    <div class="abs tile text" style="left:487px;top:824px"><h3>Interior Painting</h3><div class="bar"></div><p>Sometimes just a coat of paint is all you may need for a fresh look. Other times you need a little more.</p><a>READ MORE</a></div>
    <div class="abs tile" style="left:674px;top:824px;background:linear-gradient(180deg,#c9d6dc,#4c5754 55%,#6a7065)" role="img" aria-label="Photo of a painter working on a house exterior"></div>

    <div class="abs tile" style="left:112px;top:952px;background:linear-gradient(180deg,#c79a66,#a8754a)" role="img" aria-label="Photo of a painter rolling a ceiling in a covered room"></div>
    <div class="abs tile text" style="left:299px;top:952px"><h3>Interior Design</h3><div class="bar"></div><p>No matter what the project you can always bet there will be repairs needed to provide the best job. We</p><a>READ MORE</a></div>
    <div class="abs tile" style="left:487px;top:952px;background:linear-gradient(180deg,#ece9e2,#cfc9bd)" role="img" aria-label="Photo of two painters working in a white interior"></div>
    <div class="abs tile text" style="left:674px;top:952px"><h3>Exterior Painting</h3><div class="bar"></div><p>No matter what the project you can always bet there will be repairs needed to provide the best job. We</p><a>READ MORE</a></div>
  </section>

  <footer class="abs footer">
    <div class="abs footer-links">Home &nbsp;&nbsp;|&nbsp;&nbsp; About Us &nbsp;|&nbsp; Services &nbsp;|&nbsp; Contact Us</div>
    <div class="abs copyright">Copyright © Harlow Vance. All rights reserved</div>
  </footer>
</div>
</body>
</html>
```